Design Vitamin C serum box design and label for me

I am branding my own 20% Vitamin C Serum with Hyaluronic Acid & Vitamin E, and I need a very professional looking box design and serum bottle label to represent my product and brand! My brand name is Mira Solenne, and for the color scheme I want pink, white, and gold accents. I am attaching what my logo looks like as well as examples of the type of professionalism I am looking for. Really hope someone can put together something that I absolutely love! :)

Once I pick someone whose work I like, we can go over the details of the writing (ingredients, etc), but for now I am looking for the best front side of the box!

```html
<!DOCTYPE html>
<html lang="en">
<head>
<meta charset="UTF-8">
<title>Mira Solenne Vitamin C Serum – Box Front and Bottle Label</title>
<link rel="stylesheet" href="https://fonts.googleapis.com/css2?family=Arimo:wght@400;700&display=swap">
<style>
  :root {
    --bg: #ececee;
    --white: #ffffff;
    --pink: #d940a8;
    --pink-band: #e070c6;
    --pink-box: #dc5cbd;
    --gold: #c9a448;
    --gold-light: #e6cf80;
    --ornament: #f3c8e8;
  }
  * { box-sizing: border-box; margin: 0; padding: 0; }
  html, body { width: 1200px; height: 1200px; overflow: hidden; }
  body {
    background: var(--bg);
    font-family: "Arimo", Arial, sans-serif;
    position: relative;
  }

  /* ---------- Box front panel ---------- */
  .box-front {
    position: absolute;
    left: 150px; top: 100px;
    width: 380px; height: 1000px;
    background: var(--white);
    border-top: 12px solid var(--gold);
    border-bottom: 12px solid var(--gold);
    display: flex; flex-direction: column; align-items: center;
    box-shadow: 0 6px 24px rgba(0,0,0,0.08);
  }
  .brand {
    display: flex; flex-direction: column; align-items: center; gap: 12px;
    color: var(--gold);
  }
  .brand-mark {
    width: 26px; height: 26px; border-radius: 50%;
    background: var(--gold);
  }
  .brand-name { font-weight: 400; letter-spacing: 1px; }
  .box-front .brand { margin-top: 80px; height: 160px; }
  .box-front .brand-name { font-size: 32px; }

  .claim-band {
    width: 100%;
    background: var(--pink-band);
    border-top: 4px solid var(--gold-light);
    border-bottom: 4px solid var(--gold-light);
    color: var(--white);
    text-align: center;
    padding: 20px 0 18px;
    line-height: 1.15;
  }
  .claim-band .claim-line { font-size: 19px; letter-spacing: 2px; }
  .claim-band .claim-strong { font-size: 26px; font-weight: 700; letter-spacing: 1px; }

  .product-name {
    color: var(--pink);
    font-weight: 700;
    letter-spacing: -0.5px;
  }
  .box-front .product-name { font-size: 64px; margin-top: 44px; }

  .formula {
    border: 3px solid var(--gold);
    color: var(--pink);
    text-align: center;
    line-height: 1.15;
  }
  .box-front .formula { margin-top: 18px; padding: 14px 16px; width: 320px; }
  .formula .formula-title { font-weight: 700; font-size: 28px; letter-spacing: -0.5px; }
  .formula .formula-detail { font-size: 23px; }

  .ornament-divider {
    width: 150px; height: 30px; border-radius: 15px;
    background: var(--ornament);
  }
  .box-front .ornament-divider { margin-top: 90px; }

  .size-panel {
    background: var(--pink-box);
    border: 4px solid var(--gold);
    color: var(--white);
    display: flex; flex-direction: column; align-items: center; justify-content: center;
  }
  .box-front .size-panel {
    margin-top: auto; margin-bottom: 24px;
    width: 300px; height: 200px; gap: 40px;
  }
  .size-panel .ornament-divider { background: rgba(255,255,255,0.45); margin-top: 0; }
  .size-text { font-size: 18px; letter-spacing: 1px; }

  /* ---------- Bottle label ---------- */
  .bottle-label {
    position: absolute;
    left: 640px; top: 260px;
    width: 420px; height: 660px;
    background: var(--white);
    border-top: 8px solid var(--gold);
    border-bottom: 14px solid var(--gold);
    display: flex; flex-direction: column; align-items: center;
    box-shadow: 0 6px 24px rgba(0,0,0,0.08);
  }
  .bottle-label .brand { margin-top: 40px; gap: 10px; }
  .bottle-label .brand-mark { width: 20px; height: 20px; }
  .bottle-label .brand-name { font-size: 26px; }
  .label-claim {
    margin-top: 34px;
    text-align: center;
    color: var(--pink);
    line-height: 1.15;
  }
  .label-claim .claim-line { font-size: 21px; letter-spacing: 2px; font-weight: 700; }
  .label-claim .claim-strong { font-size: 27px; font-weight: 700; letter-spacing: 1px; }
  .bottle-label .product-name { font-size: 58px; margin-top: 28px; }
  .bottle-label .size-panel {
    margin-top: 22px; margin-bottom: 26px;
    width: 360px; flex: 1;
    justify-content: flex-start; padding-top: 18px; gap: 14px;
  }
  .bottle-label .formula-title { font-weight: 700; font-size: 32px; letter-spacing: -0.5px; text-align: center; }
  .bottle-label .formula-detail { font-size: 23px; text-align: center; line-height: 1.15; }
  .bottle-label .size-text { font-size: 15px; }
</style>
</head>
<body>

  <section class="box-front">
    <div class="brand">
      <span class="brand-mark"></span>
      <span class="brand-name">Mira Solenne</span>
    </div>

    <div class="claim-band">
      <div class="claim-line">PROFESSIONAL</div>
      <div class="claim-line">ANTI AGING</div>
      <div class="claim-strong">SERUM</div>
    </div>

    <h1 class="product-name">Vitamin C</h1>

    <div class="formula">
      <div class="formula-title">20% Vitamin C</div>
      <div class="formula-detail">Serum with Hyaluronic<br>Acid &amp; Vitamin E</div>
    </div>

    <div class="ornament-divider" role="img" aria-label="Pink swirl flourish ornament"></div>

    <div class="size-panel">
      <div class="ornament-divider" role="img" aria-label="White swirl flourish ornament"></div>
      <div class="size-text">1 FL.OZ/30 ML</div>
    </div>
  </section>

  <section class="bottle-label">
    <div class="brand">
      <span class="brand-mark"></span>
      <span class="brand-name">Mira Solenne</span>
    </div>

    <div class="label-claim">
      <div class="claim-line">PROFESSIONAL</div>
      <div class="claim-line">ANTI AGING</div>
      <div class="claim-strong">SERUM</div>
    </div>

    <h2 class="product-name">Vitamin C</h2>

    <div class="size-panel">
      <div class="formula-title">20% Vitamin C</div>
      <div class="formula-detail">Serum with Hyaluronic<br>Acid &amp; Vitamin E</div>
      <div class="ornament-divider" role="img" aria-label="White swirl flourish ornament"></div>
      <div class="size-text">1 FL.OZ/30 ML</div>
    </div>
  </section>

</body>
</html>
```